Website Design for a Law Firm

We require a fully functional Website that will be added features such as live chat, Online payment system and online forms. We need to be able to edit the website and update it regularly. We have made a website structure that is attached below.

The website footer must have:
Liability limited by a Scheme approved under Professional Standards Legislation. All legal practitioners employed by Dunmore Lawyers Pty Limited (including those described as Principal Solicitor) are members of the Scheme.

Target Market(s)

People seeking legal services in Australia

Industry/Entity Type

Legal

Coding

Coded - Design and coding required

Number of Pages Required

1 page

Requirements
Must have
• Online portal function where clients can upload documents; website that would work perfectly on standard mobile, tablet, laptop, and desktop sizes; the website must have an online payment system.
Nice to have
• Online portal function where clients

```html
<!DOCTYPE html>
<html lang="en">
<head>
<meta charset="utf-8">
<title>Dunmore Lawyers</title>
<link href="https://fonts.googleapis.com/css2?family=Libre+Baskerville:wght@400;700&family=Open+Sans:wght@400;600&display=swap" rel="stylesheet">
<style>
:root{
  --gold:#cca55f;
  --gold-soft:#d8b673;
  --green:#0d2a1c;
  --ink:#1d1d1d;
  --grey-bg:#f1f1f1;
  --footer-bg:#efefef;
  --line:#d9d9d9;
  --serif:'Libre Baskerville',Georgia,serif;
  --sans:'Open Sans',Arial,sans-serif;
}
*{margin:0;padding:0;box-sizing:border-box}
html,body{width:1200px;height:3550px;overflow:hidden}
body{position:relative;background:#fff;font-family:var(--serif);color:var(--ink)}
.abs{position:absolute}
.btn{position:absolute;display:flex;align-items:center;justify-content:center;border-radius:16px;font-family:var(--serif);font-size:12px;color:#fff;text-decoration:none}
.btn-green{background:var(--green)}
.btn-gold{background:var(--gold)}
.photo{position:absolute}

/* header */
.brand{position:absolute;left:138px;top:22px;display:flex;align-items:center;gap:8px}
.brand-dot{width:26px;height:26px;border:2px solid var(--gold);border-radius:50%}
.brand-name{font-family:var(--serif);font-size:17px;font-weight:700;color:var(--green);letter-spacing:.5px}
.topline{position:absolute;left:598px;top:29px;font-family:var(--serif);font-size:11px;color:var(--gold)}
.topline b{color:var(--ink);font-weight:400}
.nav a{position:absolute;top:72px;font-family:var(--serif);font-size:12px;color:var(--ink);text-decoration:none}
.nav a.active{color:var(--gold)}
.dropdown{position:absolute;left:485px;top:106px;width:138px;height:97px;background:var(--gold);padding:12px 12px;z-index:3}
.dropdown a{display:block;font-family:var(--serif);font-size:9px;color:#fff;line-height:18.5px;text-decoration:none}
.dropdown a.current{text-decoration:underline}

/* hero */
.hero{left:0;top:106px;width:1200px;height:487px;background:linear-gradient(135deg,#3c3a36 0%,#6b5d4b 45%,#2f3440 100%)}
.hero-title{position:absolute;left:0;width:1200px;top:284px;text-align:center;font-size:36px;line-height:44px;color:#fff}
.hero-title span{display:block;color:var(--gold-soft);font-weight:700}

/* mission */
.mission-label{left:200px;top:648px;font-size:22px;font-weight:700;color:var(--gold)}
.mission-text{left:200px;top:678px;width:340px;font-size:29px;line-height:40px}
.mission-text b{font-weight:700}
.welcome{left:550px;top:530px;width:650px;height:366px;background:var(--gold)}
.welcome h2{position:absolute;left:63px;top:66px;font-size:21px;font-weight:400;color:#fff}
.welcome h2 b{font-weight:700}
.welcome p{position:absolute;left:63px;width:400px;font-family:var(--sans);font-size:9.5px;line-height:19px;color:#fff}

/* services */
.services{left:0;top:896px;width:1200px;height:537px;background:var(--grey-bg)}
.section-title{position:absolute;left:0;width:1200px;text-align:center;font-size:30px;font-weight:400}
.section-title b{font-weight:700}
.svc{position:absolute;width:182px;height:131px;display:flex;align-items:center;justify-content:center;text-align:center;padding:0 14px;font-size:11.5px;color:#fff;line-height:14px}
.svc.dark{background:linear-gradient(135deg,#27394a,#4a5563)}
.svc.gold{background:linear-gradient(135deg,#d2ad68,#c29a55);text-decoration:underline}

/* payment band */
.pay{left:0;top:1457px;width:1200px;height:249px}
.pay-text{left:200px;top:1510px;font-size:29px;line-height:40px;color:#fff}
.pay-text b{font-weight:700}
.seal{position:absolute;border-radius:50%;background:#fff;display:flex;align-items:center;justify-content:center;gap:7px}
.seal .brand-dot{width:22px;height:22px}
.seal .brand-name{font-size:15px}

/* insights */
.insights-photo-left{left:0;top:1720px;width:138px;height:416px;background:linear-gradient(160deg,#c9b68f,#6e5a3d)}
.insights-photo-right{left:525px;top:1720px;width:675px;height:416px;background:linear-gradient(135deg,#d7dde3 0%,#9aa5b0 50%,#3a3a3a 100%)}
.insights-card{left:149px;top:1720px;width:376px;height:416px;background:#fff}
.bar-v{left:138px;top:1720px;width:11px;height:430px;background:var(--gold)}
.bar-h{left:138px;top:2139px;width:325px;height:11px;background:var(--gold)}
.ins-title{left:200px;top:1766px;font-size:30px;font-weight:400}
.ins-title b{font-weight:700}
.ins-rule{left:200px;top:1815px;width:125px;height:2px;background:var(--gold)}
.date{font-family:var(--serif);font-size:9px;font-weight:700;color:var(--gold)}
.ins-item{left:200px;width:275px;font-size:13.5px;line-height:20px}
.ins-divider{left:200px;top:1926px;width:275px;height:1px;background:var(--line)}

/* careers/costs */
.cc-title{font-size:30px;color:#fff}
.cc-text{font-family:var(--serif);font-size:13.5px;line-height:20px;color:#fff;width:290px}

/* articles */
.card{position:absolute;top:2566px;width:250px;height:324px;background:#f4f4f4;border-bottom:3px solid var(--gold)}
.card .img{position:absolute;left:0;top:0;width:250px;height:157px}
.card .date{position:absolute;left:19px;top:179px}
.card .txt{position:absolute;left:19px;top:210px;width:215px;font-size:13px;line-height:19px}
.card .more{position:absolute;left:19px;top:277px;font-size:11.5px;color:var(--gold);display:flex;align-items:center;gap:12px}
.arrow{width:30px;height:30px;border-radius:50%;border:1px solid var(--gold);display:flex;align-items:center;justify-content:center}
.arrow.filled{background:var(--gold)}

/* footer */
.footer{left:0;top:3018px;width:1200px;height:532px;background:var(--footer-bg)}
.f-head{position:absolute;top:3080px;font-size:14px;font-weight:700;color:var(--ink)}
.f-list{position:absolute;top:3119px;font-family:var(--sans);font-size:9.5px;line-height:18.8px;color:var(--ink);list-style:none}
.f-contact{position:absolute;left:138px;font-family:var(--sans);font-size:10px;line-height:18px;display:flex;gap:9px;align-items:flex-start}
.social{position:absolute;top:3258px;width:31px;height:31px;border-radius:50%;background:var(--green)}
.social.on{background:var(--gold)}
.field{position:absolute;background:#fff;border:1px solid #e2e2e2;font-family:var(--sans);font-size:9.5px;color:#555;padding:0 12px;display:flex;align-items:center}
.field.area{align-items:flex-start;padding-top:11px}
.rule{position:absolute;left:138px;width:924px;height:1px;background:var(--line)}
.liability{position:absolute;left:240px;top:3365px;width:720px;text-align:center;font-family:var(--sans);font-size:8.5px;line-height:18px;color:var(--ink)}
.bottom{position:absolute;top:3478px;font-family:var(--sans);font-size:10px;color:var(--ink)}
.paycard{position:absolute;top:3472px;width:40px;height:27px;border-radius:3px;background:#fff;border:1px solid #cfcfcf;font-family:var(--sans);font-size:7px;font-weight:600;color:var(--green);display:flex;align-items:center;justify-content:center}
.chat{position:absolute;left:1100px;top:2985px;width:62px;height:62px;border-radius:50%;background:var(--gold);display:flex;align-items:center;justify-content:center}
</style>
</head>
<body>

<!-- header -->
<header>
  <div class="brand"><span class="brand-dot"></span><span class="brand-name">DUNMORE</span></div>
  <div class="topline">Call us Today at <b>&#9742; 555-010-2468</b></div>
  <a class="btn btn-green" style="left:787px;top:21px;width:157px;height:30px">Book An Appointments</a>
  <a class="btn btn-gold" style="left:958px;top:21px;width:104px;height:30px">Client Login</a>
  <nav class="nav">
    <a style="left:435px">Home</a>
    <a class="active" style="left:499px">About Us &#709;</a>
    <a style="left:591px">Our Services &#709;</a>
    <a style="left:701px">Insights &amp; News</a>
    <a style="left:820px">Careers</a>
    <a style="left:890px">Costs</a>
    <a style="left:951px">Blog</a>
    <a style="left:1004px">Contact Us</a>
  </nav>
  <div class="dropdown">
    <a>Our History</a>
    <a>Our Promise To You</a>
    <a class="current">Our People</a>
    <a>Mission &amp; Vision Statement</a>
  </div>
</header>

<!-- hero -->
<section class="photo hero abs" role="img" aria-label="Photo of lawyers in discussion around a table"></section>
<h1 class="hero-title">Hard work delivers<span>elite results</span></h1>
<a class="btn btn-gold" style="left:544px;top:390px;width:112px;height:30px">Contact Us</a>

<!-- mission + welcome -->
<div class="abs mission-label">Mission &amp; Vision Statement</div>
<p class="abs mission-text">Lorem Ipsum is <b>simply dummy text</b> of the printing and <b>typesetting industry</b> Ipsum.</p>
<section class="abs welcome">
  <h2>Welcome to <b>Dunmore Lawyers</b></h2>
  <p style="top:114px">Lorem Ipsum is simply dummy text of the printing and typesetting industry. Lorem Ipsum has been the industry's standard dummy text ever since the 1500s, when an unknown printer took a galley of type and scrambled it to make a type specimen book.</p>
  <p style="top:203px">If you are going to use a passage of Lorem Ipsum, you need to be sure there isn't anything embarrassing hidden in the middle of text ...</p>
  <a class="btn btn-green" style="left:63px;top:270px;width:112px;height:31px">Explore More</a>
</section>

<!-- services -->
<section class="abs services"></section>
<h2 class="section-title" style="top:962px">Our <b>services</b></h2>
<div class="svc dark" style="left:200px;top:1044px" role="img" aria-label="Administrative law photo">Administrative Law</div>
<div class="svc gold" style="left:406px;top:1044px" role="img" aria-label="Commercial law photo">Commercial Law</div>
<div class="svc dark" style="left:612px;top:1044px" role="img" aria-label="Property law photo">Property Law</div>
<div class="svc dark" style="left:818px;top:1044px" role="img" aria-label="Immigration law photo">Immigration Law</div>
<div class="svc dark" style="left:200px;top:1200px" role="img" aria-label="Employment law photo">Employment Law</div>
<div class="svc dark" style="left:406px;top:1200px" role="img" aria-label="Family and relationship law photo">Family &amp; Relationship Law</div>
<div class="svc dark" style="left:612px;top:1200px" role="img" aria-label="Criminal law photo">Criminal</div>
<div class="svc dark" style="left:818px;top:1200px" role="img" aria-label="Professional misconduct photo">Professional Misconduct</div>
<a class="btn btn-gold" style="left:522px;top:1357px;width:156px;height:32px">Book An Appointments</a>

<!-- payment -->
<svg class="abs pay" width="1200" height="249" viewBox="0 0 1200 249">
  <rect width="1200" height="249" fill="#cca55f"/>
  <polygon points="834,0 1200,0 1200,249 813,249" fill="#0d2a1c"/>
</svg>
<p class="abs pay-text">You can process <b>payment online</b><br>using our payment portal.</p>
<a class="btn btn-green" style="left:200px;top:1623px;width:113px;height:31px">Pay Now</a>
<div class="seal" style="left:726px;top:1487px;width:190px;height:190px"><span class="brand-dot"></span><span class="brand-name">DUNMORE</span></div>

<!-- insights -->
<div class="abs insights-photo-left" role="img" aria-label="Photo of law books and scales"></div>
<div class="abs insights-photo-right" role="img" aria-label="Photo of a judge's gavel on a desk"></div>
<div class="abs insights-card"></div>
<div class="abs bar-v"></div>
<div class="abs bar-h"></div>
<h2 class="abs ins-title">Insights &amp; <b>news</b></h2>
<div class="abs ins-rule"></div>
<div class="abs date" style="left:200px;top:1838px">DEC-20-2022</div>
<p class="abs ins-item" style="top:1871px">Contrary to popular belief, Lorem Ipsum is not simply random text.</p>
<div class="abs ins-divider"></div>
<div class="abs date" style="left:200px;top:1953px">DEC-20-2022</div>
<p class="abs ins-item" style="top:1985px">Contrary to popular belief, Lorem Ipsum is not simply random text.</p>
<a class="btn btn-green" style="left:200px;top:2053px;width:113px;height:30px">See More</a>

<!-- careers / costs -->
<svg class="abs" style="left:0;top:2183px" width="1200" height="249" viewBox="0 0 1200 249" role="img" aria-label="Photos of a handshake over legal documents">
  <defs>
    <linearGradient id="careersTone" x1="0" y1="0" x2="1" y2="1"><stop offset="0" stop-color="#27443a"/><stop offset="1" stop-color="#0f2a1e"/></linearGradient>
    <linearGradient id="costsTone" x1="0" y1="0" x2="1" y2="1"><stop offset="0" stop-color="#d3b06f"/><stop offset="1" stop-color="#c29a55"/></linearGradient>
  </defs>
  <rect width="1200" height="249" fill="url(#costsTone)"/>
  <polygon points="0,0 627,0 572,249 0,249" fill="url(#careersTone)"/>
</svg>
<div class="abs cc-title" style="left:138px;top:2230px">Careers</div>
<p class="abs cc-text" style="left:138px;top:2288px">Contrary to popular belief, lorem ipsum is not simply random text.</p>
<a class="btn btn-gold" style="left:138px;top:2359px;width:111px;height:32px">Find a Job</a>
<div class="abs cc-title" style="left:788px;top:2230px">Costs</div>
<p class="abs cc-text" style="left:788px;top:2288px">Contrary to popular belief, lorem ipsum is not simply random text.</p>
<a class="btn btn-green" style="left:788px;top:2359px;width:112px;height:31px">Get a Costs</a>
<div class="seal" style="left:504px;top:2213px;width:190px;height:190px"><span class="brand-dot"></span><span class="brand-name">DUNMORE</span></div>

<!-- articles -->
<h2 class="section-title" style="top:2498px">Recent <b>articles</b></h2>
<article class="card" style="left:200px">
  <div class="img" role="img" aria-label="Photo of a team meeting at a table" style="background:linear-gradient(135deg,#4f4a45,#b9a78f)"></div>
  <div class="date">DEC-20-2022</div>
  <p class="txt">There are many variations lorem Ipsum available ...</p>
  <div class="more">Read More <span class="arrow filled"><svg width="8" height="8" viewBox="0 0 8 8"><path d="M2 1l3 3-3 3" stroke="#fff" fill="none"/></svg></span></div>
</article>
<article class="card" style="left:475px">
  <div class="img" role="img" aria-label="Photo of a gavel beside a laptop" style="background:linear-gradient(135deg,#6a5a4a,#c8c2b8)"></div>
  <div class="date">JAN-12-2023</div>
  <p class="txt">There are many variations lorem Ipsum available ...</p>
  <div class="more">Read More <span class="arrow"><svg width="8" height="8" viewBox="0 0 8 8"><path d="M2 1l3 3-3 3" stroke="#cca55f" fill="none"/></svg></span></div>
</article>
<article class="card" style="left:750px">
  <div class="img" role="img" aria-label="Photo of a person signing documents" style="background:linear-gradient(135deg,#2c2a27,#7a6a55)"></div>
  <div class="date">FEB-14-2023</div>
  <p class="txt">There are many variations lorem Ipsum available ...</p>
  <div class="more">Read More <span class="arrow"><svg width="8" height="8" viewBox="0 0 8 8"><path d="M2 1l3 3-3 3" stroke="#cca55f" fill="none"/></svg></span></div>
</article>
<a class="btn btn-green" style="left:550px;top:2924px;width:113px;height:31px">View All</a>

<!-- footer -->
<footer>
  <div class="abs footer"></div>
  <div class="chat"><svg width="26" height="24" viewBox="0 0 26 24"><path d="M3 2h20v15H9l-6 5z" fill="#fff"/><path d="M9 12l7-7 2 2-7 7H9z" fill="#cca55f"/></svg></div>

  <div class="f-head" style="left:138px">Contact Us</div>
  <div class="f-head" style="left:343px">Quick Links</div>
  <div class="f-head" style="left:511px">Our Services</div>
  <div class="f-head" style="left:712px">Book An Appointments</div>

  <div class="f-contact" style="top:3124px;font-family:var(--serif);font-size:14px">
    <svg width="12" height="12" viewBox="0 0 12 12" style="margin-top:3px"><path d="M2 1l2 0 1 3-1.5 1a6 6 0 003 3L8 7l3 1v2c0 1-1 1-1 1A9 9 0 011 2s0-1 1-1z" fill="#cca55f"/></svg>
    <span>555-010-2468</span>
  </div>
  <div class="f-contact" style="top:3157px">
    <svg width="12" height="10" viewBox="0 0 12 10" style="margin-top:4px"><rect width="12" height="10" rx="1" fill="#cca55f"/><path d="M0 1l6 4 6-4" stroke="#fff" fill="none"/></svg>
    <span>info@dunmorelawyers.com</span>
  </div>
  <div class="f-contact" style="top:3188px">
    <svg width="10" height="13" viewBox="0 0 10 13" style="margin-top:3px"><path d="M5 0a5 5 0 015 5c0 4-5 8-5 8S0 9 0 5a5 5 0 015-5z" fill="#cca55f"/><circle cx="5" cy="5" r="2" fill="#efefef"/></svg>
    <span>Lorem 302, 3. kat,<br>G 2 Zgrada br. 03 Lorem ipsum,<br>Dolor, Sit-Amet, 12345</span>
  </div>
  <span class="social" style="left:137px" aria-label="Social profile"></span>
  <span class="social on" style="left:175px" aria-label="Social profile"></span>
  <span class="social" style="left:214px" aria-label="Social profile"></span>

  <ul class="f-list" style="left:343px">
    <li>Home</li><li>About Us</li><li>Our Services</li><li>Insights &amp; News</li><li>Careers</li><li>Costs</li><li>Blog</li><li>Contact Us</li><li>Online pay</li>
  </ul>
  <ul class="f-list" style="left:511px">
    <li>Administrative law</li><li>Commercial Law</li><li>Property Law</li><li>Immigration Law</li><li>Employment Law</li><li>Family &amp; Relationship Law</li><li>Criminal</li><li>Professional Misconduct</li>
  </ul>

  <div class="field" style="left:712px;top:3122px;width:170px;height:31px">Name</div>
  <div class="field" style="left:894px;top:3122px;width:168px;height:31px">Phone</div>
  <div class="field" style="left:712px;top:3165px;width:350px;height:31px">Email</div>
  <div class="field area" style="left:712px;top:3211px;width:350px;height:59px">Message</div>
  <a class="btn btn-green" style="left:712px;top:3285px;width:113px;height:30px">Send</a>

  <div class="rule" style="top:3340px"></div>
  <p class="liability">Liability limited by a Scheme approved under Professional Standards Legislation. All legal practitioners employed by Dunmore Lawyers Pty Limited (including those described as Principal Solicitor) are members of the Scheme.</p>
  <div class="rule" style="top:3416px"></div>

  <div class="abs" style="left:138px;top:3455px;width:62px;height:62px;border:3px solid var(--gold);border-radius:50%"></div>
  <div class="bottom" style="left:231px">&copy; 2023 <span style="color:var(--gold)">Dunmore Lawyers</span>. All Right Reserved</div>
  <div class="bottom" style="left:511px">Compliance &nbsp;&nbsp; / &nbsp;&nbsp; Disclaimers</div>
  <div class="bottom" style="left:712px;font-family:var(--serif);font-size:11px">We Accept</div>
  <span class="paycard" style="left:788px">Paycard</span>
  <span class="paycard" style="left:832px">Novacard</span>
  <span class="paycard" style="left:876px">Meridian</span>
  <span class="paycard" style="left:920px">Orbit</span>
  <span class="paycard" style="left:964px">Walletly</span>
</footer>

</body>
</html>
```